Bilingual school website redesign

The website oruvabilingualschool.example needs a new design

It is a private school from pre kinder to third grade

They teach Spanish and English

In the same website there is a section where teachers and parents interact
Updates

Reason: We are still waiting for approval from the school's teachers.

Target Market(s)

Mostly students' parents

Industry/Entity Type

Education

Number of Pages Required

3 page

Font styles to use
Sans Serif

Requirements
Must have
• Photo gallery
• Responsive design

```html
<!DOCTYPE html>
<html lang="es">
<head>
<meta charset="utf-8">
<title>Oruva Bilingual School</title>
<link href="https://fonts.googleapis.com/css2?family=Open+Sans:wght@400;600;700&display=swap" rel="stylesheet">
<style>
  :root {
    --blue-dark: #1a63c4;
    --blue: #2d86e0;
    --blue-text: #1f7fd6;
    --red: #e1262b;
    --red-dark: #b91c20;
    --ink: #333333;
    --muted: #777777;
    --panel: #eeeeee;
    --footer: #3b3b3b;
    --white: #ffffff;
    --button: #262626;
  }
  * { box-sizing: border-box; margin: 0; padding: 0; }
  html, body { width: 795px; height: 1200px; overflow: hidden; }
  body { font-family: "Open Sans", Arial, sans-serif; color: var(--ink); background: var(--white); position: relative; }

  .site-header { height: 80px; background: linear-gradient(180deg, var(--blue-dark), var(--blue)); position: relative; }
  .brand { position: absolute; left: 34px; top: 14px; display: flex; align-items: center; gap: 8px; }
  .brand-mark { width: 26px; height: 26px; border-radius: 50%; background: var(--white); }
  .brand-name { color: var(--white); font-weight: 700; font-size: 20px; letter-spacing: 1px; }
  .contact { position: absolute; right: 40px; top: 14px; text-align: right; color: var(--white); }
  .contact .hours { font-size: 9px; opacity: .9; }
  .contact .phone { font-size: 15px; font-weight: 700; margin-top: 2px; }

  .main-nav { height: 36px; background: var(--red); display: flex; align-items: stretch; padding-left: 44px; position: relative; }
  .main-nav a { color: var(--white); text-decoration: none; font-size: 11px; font-weight: 600; padding: 0 16px; display: flex; align-items: center; border-right: 1px solid var(--red-dark); }
  .main-nav .lang { position: absolute; right: 40px; top: 10px; width: 26px; height: 16px; background: var(--white); border-radius: 2px; }

  .hero { height: 308px; position: relative; background: linear-gradient(120deg, #cfd8de 0%, #e9ecee 40%, #f3f1ec 60%, #d7dde0 100%); }
  .hero-box { position: absolute; left: 62px; top: 70px; width: 243px; height: 160px; background: var(--blue); padding: 18px 20px; color: var(--white); }
  .hero-box h1 { font-size: 22px; font-weight: 700; line-height: 1.2; }
  .hero-box p { font-size: 9px; margin-top: 8px; line-height: 1.4; opacity: .9; }
  .btn { display: inline-block; background: var(--button); color: var(--white); font-size: 9px; padding: 5px 11px; border-radius: 2px; margin-top: 10px; }
  .arrow { position: absolute; top: 138px; width: 22px; height: 30px; background: rgba(40,40,40,.75); }
  .arrow.prev { left: 0; } .arrow.next { right: 0; }
  .arrow svg { display: block; margin: 9px auto; }

  .welcome { height: 136px; text-align: center; padding-top: 22px; }
  .welcome h2 { font-size: 28px; font-weight: 400; color: var(--ink); }
  .welcome p { width: 600px; margin: 10px auto 0; font-size: 9px; color: var(--muted); line-height: 1.5; }
  .welcome .btn { margin-top: 8px; }

  .services { height: 345px; background: var(--panel); padding: 30px 60px 0; position: relative; }
  .section-title { font-size: 22px; font-weight: 400; color: var(--ink); }
  .carousel-nav { position: absolute; right: 62px; top: 38px; display: flex; gap: 6px; }
  .cards { display: flex; gap: 15px; margin-top: 22px; }
  .card { width: 215px; }
  .card-photo { height: 100px; }
  .card h3 { color: var(--blue-text); font-size: 17px; font-weight: 400; margin-top: 12px; white-space: nowrap; }
  .card p { font-size: 9px; color: var(--muted); line-height: 1.45; margin-top: 5px; }
  .card .btn { margin-top: 8px; }

  .promotions { height: 240px; padding: 30px 60px 0; }
  .promo-grid { display: flex; gap: 14px; margin-top: 20px; }
  .promo { width: 158px; }
  .promo-photo { height: 70px; }
  .promo h4 { color: var(--blue-text); font-size: 13px; font-weight: 400; line-height: 1.2; margin-top: 8px; }
  .promo time { display: block; font-size: 8px; color: var(--muted); margin-top: 4px; }

  .site-footer { position: absolute; left: 0; bottom: 0; width: 795px; height: 55px; background: var(--footer); color: #cccccc; padding: 10px 60px 0; }
  .footer-nav { display: flex; gap: 30px; font-size: 8px; }
  .copyright { font-size: 7px; margin-top: 8px; color: #aaaaaa; }
  .social { position: absolute; right: 60px; top: 14px; display: flex; gap: 8px; }
  .social span { width: 18px; height: 18px; border-radius: 2px; }
</style>
</head>
<body>
  <header class="site-header">
    <div class="brand"><span class="brand-mark"></span><span class="brand-name">ORUVA</span></div>
    <div class="contact">
      <div class="hours">Horario: Lunes a Viernes de 7:00 a.m. a 3:00 p.m.</div>
      <div class="phone">5550-1234, 5550-5678</div>
    </div>
  </header>

  <nav class="main-nav">
    <a>INICIO</a><a>NUESTRA ESCUELA</a><a>NOTICIAS</a><a>ACTIVIDADES</a><a>RECURSOS EN LINEA</a><a>CONTÁCTENOS</a>
    <span class="lang"></span>
  </nav>

  <section class="hero" role="img" aria-label="Photo of a teacher with cheerful young students raising their hands in a classroom">
    <div class="hero-box">
      <h1>100% BILINGUAL<br>EDUCATION</h1>
      <p>Clases en inglés y español desde pre kinder hasta tercer grado con maestros dedicados.</p>
      <span class="btn">Read More</span>
    </div>
    <span class="arrow prev"><svg width="6" height="12" viewBox="0 0 6 12"><path d="M5 1 1 6l4 5" stroke="#fff" stroke-width="2" fill="none"/></svg></span>
    <span class="arrow next"><svg width="6" height="12" viewBox="0 0 6 12"><path d="M1 1l4 5-4 5" stroke="#fff" stroke-width="2" fill="none"/></svg></span>
  </section>

  <section class="welcome">
    <h2>Welcome to ORUVA</h2>
    <p>Oruva Bilingual School nace como un proyecto educativo para ofrecer a cada niño una formación completa en dos idiomas, con grupos pequeños, atención personal y un ambiente seguro, alegre y cercano a las familias de nuestra comunidad.</p>
    <span class="btn">Read More</span>
  </section>

  <section class="services">
    <h2 class="section-title">Our Services</h2>
    <div class="carousel-nav">
      <svg width="8" height="12" viewBox="0 0 8 12"><path d="M6 1 2 6l4 5" stroke="#333" stroke-width="2" fill="none"/></svg>
      <svg width="8" height="12" viewBox="0 0 8 12"><path d="M2 1l4 5-4 5" stroke="#333" stroke-width="2" fill="none"/></svg>
    </div>
    <div class="cards">
      <article class="card">
        <div class="card-photo" role="img" aria-label="Photo of children studying together" style="background:linear-gradient(135deg,#5aa6e0,#f0c04a)"></div>
        <h3>Educación 100% bilingüe</h3>
        <p>Aprendizaje diario en ambos idiomas con actividades, juegos y lecturas guiadas.</p>
        <span class="btn">Read More</span>
      </article>
      <article class="card">
        <div class="card-photo" role="img" aria-label="Photo of colourful letter blocks on a table" style="background:linear-gradient(135deg,#4a4a4a,#c9a23a 60%,#7a9ac0)"></div>
        <h3>Textos completamente</h3>
        <p>Libros y materiales preparados para cada grado, todos en dos idiomas.</p>
        <span class="btn">Read More</span>
      </article>
      <article class="card">
        <div class="card-photo" role="img" aria-label="Photo of students in front of a classroom chalkboard" style="background:linear-gradient(135deg,#3f6e4f,#d9b48a 55%,#e36a4a)"></div>
        <h3>Transporte privado</h3>
        <p>Rutas seguras en la ciudad con monitores que acompañan cada viaje.</p>
        <span class="btn">Read More</span>
      </article>
    </div>
  </section>

  <section class="promotions">
    <h2 class="section-title">Our Promotions</h2>
    <div class="promo-grid">
      <article class="promo">
        <div class="promo-photo" role="img" aria-label="Promotional flyer photo" style="background:linear-gradient(135deg,#2f6fc4,#e24a4a)"></div>
        <h4>Haga click sobre la foto para ver la galería.</h4>
        <time>Ago 19, 2013</time>
      </article>
      <article class="promo">
        <div class="promo-photo" role="img" aria-label="Promotional flyer photo" style="background:linear-gradient(135deg,#f0d24a,#e06a3a)"></div>
        <h4>Haga click sobre la foto para ver la galería.</h4>
        <time>Ago 19, 2013</time>
      </article>
      <article class="promo">
        <div class="promo-photo" role="img" aria-label="Promotional flyer photo" style="background:linear-gradient(135deg,#1e3a5a,#3a8a4a)"></div>
        <h4>Haga click sobre la foto para ver la galería.</h4>
        <time>Ago 19, 2013</time>
      </article>
      <article class="promo">
        <div class="promo-photo" role="img" aria-label="Promotional flyer photo" style="background:linear-gradient(135deg,#1a2a3a,#4a6a9a)"></div>
        <h4>Haga click sobre la foto para ver la galería.</h4>
        <time>Ago 19, 2013</time>
      </article>
    </div>
  </section>

  <footer class="site-footer">
    <div class="footer-nav"><span>INICIO</span><span>NUESTRA ESCUELA</span><span>NOTICIAS</span><span>ACTIVIDADES</span><span>RECURSOS EN LINEA</span><span>CONTÁCTENOS</span></div>
    <div class="copyright">© 2013 ORUVA. ALL RIGHTS RESERVED</div>
    <div class="social"><span style="background:#3b5a9a"></span><span style="background:#f28a1e"></span><span style="background:#2aa9e0"></span></div>
  </footer>
</body>
</html>
```